Body therapist needs a business card

I need a card for my business which is teaching trainings in body therapy, the company is called Wexcombe Educational Group. I teach to massage therapists around Australia, South East Asia and the USA. I am attaching my logo which will guide you as to what colours I would like to have you consider. Please consult my website to find out more about what I do. www.corvantela.com.au

My name is Daniel Wexcombe. My phone number is (03) 9417 2608 or 0461753208. email is info@corvantela.com.au

```html
<!DOCTYPE html>
<html lang="en">
<head>
<meta charset="utf-8">
<title>Wexcombe Educational Group – Business Card</title>
<link href="https://fonts.googleapis.com/css2?family=Lato:wght@400;700;900&display=swap" rel="stylesheet">
<style>
  :root {
    --brown: #5c3324;
    --lime: #c8dc2c;
    --red: #b31f25;
    --white: #ffffff;
    --stage: #e9e7e4;
  }
  * { margin: 0; padding: 0; box-sizing: border-box; }
  html, body { width: 1200px; height: 900px; overflow: hidden; background: var(--stage); }
  body { position: relative; font-family: "Lato", sans-serif; }

  .card {
    position: absolute;
    width: 620px;
    height: 354px;
    border-radius: 26px;
    overflow: hidden;
    box-shadow: 0 10px 24px rgba(0,0,0,0.18);
  }

  /* Front */
  .card-front { left: 80px; top: 56px; background: var(--brown); }
  .brand {
    position: absolute;
    left: 70px; top: 146px;
    display: flex; align-items: center; gap: 20px;
  }
  .brand-dot { width: 56px; height: 56px; border-radius: 50%; background: var(--lime); flex: none; }
  .brand-name { color: var(--white); font-weight: 400; font-size: 32px; letter-spacing: 0.3px; white-space: nowrap; }

  /* Back */
  .card-back { left: 500px; top: 490px; background: var(--white); }
  .card-back .wave { position: absolute; inset: 0; }
  .person { position: absolute; left: 40px; top: 96px; }
  .person-name { color: var(--brown); font-weight: 900; font-size: 31px; line-height: 1.1; }
  .person-role { color: var(--red); font-weight: 400; font-size: 17px; margin-top: 4px; margin-left: 18px; }

  .contact { position: absolute; left: 190px; top: 228px; color: var(--white); font-size: 13px; line-height: 17px; }
  .contact-company { color: var(--lime); font-weight: 700; font-size: 14px; }
  .contact-address { margin-left: 8px; }
  .contact-list { list-style: none; margin-top: 6px; }
  .contact-list li { display: flex; align-items: center; gap: 10px; }
  .contact-list svg { width: 13px; height: 13px; flex: none; }
</style>
</head>
<body>

  <section class="card card-front" aria-label="Card front">
    <div class="brand">
      <span class="brand-dot"></span>
      <span class="brand-name">Wexcombe Educational Group</span>
    </div>
  </section>

  <section class="card card-back" aria-label="Card back">
    <svg class="wave" viewBox="0 0 620 354" preserveAspectRatio="none">
      <path d="M70 354 C90 260 170 200 330 190 C500 180 590 150 620 60 L620 354 Z" fill="var(--brown)"/>
      <path d="M52 354 C72 252 156 184 330 178" fill="none" stroke="var(--lime)" stroke-width="7"/>
    </svg>

    <div class="person">
      <p class="person-name">Daniel Wexcombe</p>
      <p class="person-role">Founder &amp; Trainer</p>
    </div>

    <div class="contact">
      <p class="contact-company">Wexcombe Educational Group</p>
      <p class="contact-address">P.O. Box 2748 Ashvale North<br>Victoria, 3189 Australia</p>
      <ul class="contact-list">
        <li>
          <svg viewBox="0 0 16 16"><path d="M4 1 L6.5 4 L5 6 C6 8 8 10 10 11 L12 9.5 L15 12 L13 15 C7 14 2 9 1 3 Z" fill="var(--lime)"/></svg>
          (03) 9417 2608
        </li>
        <li>
          <svg viewBox="0 0 16 16"><rect x="1" y="3" width="14" height="10" fill="var(--lime)"/><path d="M1 3 L8 9 L15 3" fill="none" stroke="var(--brown)" stroke-width="1.4"/></svg>
          info@corvantela.com.au
        </li>
        <li>
          <svg viewBox="0 0 16 16"><circle cx="8" cy="8" r="6.5" fill="none" stroke="var(--lime)" stroke-width="1.5"/><path d="M1.5 8 H14.5 M8 1.5 C4.5 5 4.5 11 8 14.5 M8 1.5 C11.5 5 11.5 11 8 14.5" fill="none" stroke="var(--lime)" stroke-width="1.2"/></svg>
          www.corvantela.com.au
        </li>
      </ul>
    </div>
  </section>

</body>
</html>
```